Podcast cover art (not a logo)

I’m launching an audio-only podcast for parents of neurodivergent children. The podcast is meant to feel like a calm, trusted professional voice — not a brand or a performance.

Style direction:
--Clean and minimal
--Calm and grounded
--Professional, not playful
--Nothing flashy, loud, or busy
--No cartoon imagery

Content on the cover:
--Podcast title: Under the Quiet Surface
--Subtitle or tagline: Supporting Neurodivergent Kids with Science, Not Shame (or Understanding Neurodivergent Kids)
--No episode numbers, no dates

Design preferences:
--Text-forward design
--Neutral or soft colors (muted blues, grays, off-whites)
--High contrast for readability at small sizes
--Simple, timeless font

What I do NOT want:
--A logo or branding system
--Illustrations of children or families
--Bright colors or playful graphics
--Trendy fonts or visual effects

Technical requirements:
--Square image
--3000 × 3000 pixels
--RGB color mode
--JPEG or PNG
--File size under 500 KB

Deliverables:
--Final cover art file
--Optional: one or two alternate background color versions

```html
<!DOCTYPE html>
<html lang="en">
<head>
<meta charset="utf-8">
<title>Under the Quiet Surface — Podcast Cover</title>
<link rel="stylesheet" href="https://fonts.googleapis.com/css2?family=Anton&family=Poppins:wght@400;600&display=swap">
<style>
  :root {
    --teal-deep: #15292f;
    --teal-mid: #1f3f47;
    --teal-light: #254b54;
    --title-white: #ffffff;
    --accent-blue: #96b8cc;
    --soft-grey: #d6e0e5;
  }
  html, body {
    margin: 0;
    padding: 0;
    width: 1200px;
    height: 1200px;
    overflow: hidden;
    background: var(--teal-deep);
  }
  .cover {
    position: relative;
    width: 1200px;
    height: 1200px;
    overflow: hidden;
  }
  .cover__backdrop {
    position: absolute;
    inset: 0;
    background: radial-gradient(ellipse at 40% 30%, var(--teal-light) 0%, var(--teal-mid) 45%, var(--teal-deep) 100%);
  }
  .cover__art {
    position: absolute;
    inset: 0;
    width: 1200px;
    height: 1200px;
  }
  .title-kicker {
    font-family: "Poppins", "Helvetica Neue", sans-serif;
    font-weight: 600;
    font-size: 44px;
    letter-spacing: 0.35em;
    fill: var(--accent-blue);
  }
  .title-word {
    font-family: "Anton", "Impact", sans-serif;
    font-size: 250px;
    fill: var(--title-white);
  }
  .title-rule { fill: var(--accent-blue); }
  .tagline {
    font-family: "Poppins", "Helvetica Neue", sans-serif;
    font-weight: 400;
    font-size: 34px;
    letter-spacing: 0.04em;
    fill: var(--soft-grey);
  }
</style>
</head>
<body>
<main class="cover">
  <div class="cover__backdrop" role="img" aria-label="Soft muted teal background"></div>

  <svg class="cover__art" viewBox="0 0 1200 1200" xmlns="http://www.w3.org/2000/svg" aria-labelledby="cover-title">
    <title id="cover-title">Under the Quiet Surface — Understanding Neurodivergent Kids</title>
    <defs>
      <filter id="title-shadow" x="-10%" y="-20%" width="120%" height="140%">
        <feDropShadow dx="0" dy="4" stdDeviation="10" flood-color="#0b1c21" flood-opacity="0.7"/>
      </filter>
    </defs>

    <text class="title-kicker" x="615" y="320" text-anchor="middle">UNDER THE</text>

    <g class="title" filter="url(#title-shadow)">
      <text class="title-word" x="600" y="580" text-anchor="middle">QUIET</text>
      <text class="title-word" x="600" y="840" text-anchor="middle">SURFACE</text>
    </g>

    <rect class="title-rule" x="540" y="900" width="120" height="6"/>

    <text class="tagline" x="600" y="975" text-anchor="middle">Understanding Neurodivergent Kids</text>
  </svg>
</main>
</body>
</html>
```